coaching agenda

Please redesign the brochure attached in a more modern/trendy out look. I want something completely different to what is attached but using the same colours and logo.

```html
<!DOCTYPE html>
<html lang="en">
<head>
<meta charset="utf-8">
<title>Coaching Session – June 2018</title>
<link href="https://fonts.googleapis.com/css2?family=Open+Sans:ital,wght@0,400;0,600;0,700;1,400&family=Montserrat:wght@600;700&family=Playfair+Display:wght@700&display=swap" rel="stylesheet">
<style>
:root{
  --blue:#3a9ad9;
  --blue-dark:#2478b5;
  --band:#5a5d62;
  --ink:#2d2f33;
  --text:#5c6066;
  --muted:#9aa0a6;
  --paper:#ffffff;
  --stage:#f2f3f5;
  --photo-a:#c9d7e3;
  --photo-b:#8fa6ba;
}
*{box-sizing:border-box;margin:0;padding:0}
html,body{width:1200px;height:3913px;overflow:hidden;background:var(--stage);font-family:"Open Sans",Arial,sans-serif;color:var(--text)}
.canvas{position:relative;width:1200px;height:3913px}
.sheet{position:absolute;height:707px;display:flex;box-shadow:0 10px 30px rgba(0,0,0,.12)}
.sheet--single{left:350px;width:500px}
.sheet--spread{left:100px;width:1000px}
.page{position:relative;width:500px;height:707px;background:var(--paper);overflow:hidden}
.page + .page{border-left:1px solid #e4e6e9}
.photo{position:absolute;background:linear-gradient(135deg,var(--photo-a),var(--photo-b))}
.photo--warm{background:linear-gradient(135deg,#d9dde2,#7d8894)}
.photo--dark{background:linear-gradient(160deg,#9aa5b0,#3f4852)}
.url{position:absolute;top:26px;right:34px;font-size:9px;color:var(--muted);letter-spacing:.5px}
.brand{position:absolute;display:flex;align-items:center;gap:8px}
.brand__mark{width:26px;height:26px;background:var(--ink)}
.brand__name{font-family:"Montserrat",Arial,sans-serif;font-weight:700;font-size:14px;color:var(--ink)}
.brand--sm .brand__mark{width:14px;height:14px}
.brand--sm .brand__name{font-size:9px}
.band{position:absolute;background:var(--band);color:#fff;font-family:"Montserrat",Arial,sans-serif;font-weight:700;text-transform:uppercase;line-height:1.2;padding:16px 22px;font-size:19px}
.title{position:absolute;font-family:"Playfair Display",Georgia,serif;font-weight:700;color:var(--ink);text-transform:uppercase;line-height:1.05}
.title__main{font-size:30px;display:block}
.title__date{font-size:34px;color:var(--blue);display:block;margin-top:4px;font-family:"Montserrat",Arial,sans-serif}
.rule{position:absolute;height:3px;background:var(--ink)}
.quote{position:absolute;background:var(--blue);color:#fff;padding:20px 22px 20px 30px;font-weight:700;font-size:14px;line-height:1.35}
.quote__mark{position:absolute;left:10px;top:6px;font-size:26px;font-family:"Playfair Display",Georgia,serif}
.quote__by{display:block;margin-top:8px;font-weight:400;font-size:8px;opacity:.85}
.heading{position:absolute;font-family:"Montserrat",Arial,sans-serif;font-weight:700;color:var(--ink);text-transform:uppercase;font-size:18px;border-left:4px solid var(--blue);padding-left:8px}
.copy{position:absolute;font-size:7.5px;line-height:1.6;color:var(--text)}
.copy p + p{margin-top:7px}
.section-title{position:absolute;border-left:4px solid var(--blue);padding-left:10px;font-family:"Montserrat",Arial,sans-serif;font-weight:700;font-size:19px;color:var(--ink);line-height:1.2}
.lead{position:absolute;font-size:9px;line-height:1.5;font-style:italic;color:var(--blue);font-weight:600}
.ideas{position:absolute;list-style:none;display:grid;grid-template-columns:1fr 1fr;column-gap:22px;row-gap:12px}
.ideas li{display:flex;align-items:center;gap:8px;font-size:8px;color:var(--ink);line-height:1.3}
.ideas__num{flex:none;width:20px;height:20px;border-radius:50%;background:var(--blue);color:#fff;font-weight:700;font-size:9px;display:flex;align-items:center;justify-content:center}
.footer-bar{position:absolute;bottom:22px;height:8px;background:var(--blue)}
.footer-bar::after{content:"";position:absolute;right:6px;top:2px;width:4px;height:4px;background:#fff}
.callout{position:absolute;background:var(--blue);color:#fff;font-weight:700;font-size:12px;line-height:1.35;padding:14px 18px}
.questions{position:absolute;list-style:none}
.questions li{font-family:"Montserrat",Arial,sans-serif;font-weight:700;color:var(--blue);font-size:12.5px;line-height:1.3;margin-bottom:10px}
.questions li span{color:var(--ink)}
.checklist{list-style:none;font-size:7.5px;line-height:1.7;color:var(--ink);margin:-4px 0 10px 18px}
.checklist li{font-family:"Open Sans",Arial,sans-serif;font-weight:400;color:var(--ink);font-size:7.5px;margin:0}
.checklist li::before{content:"";display:inline-block;width:5px;height:5px;background:var(--blue);margin-right:6px}
.subhead{font-family:"Montserrat",Arial,sans-serif;font-weight:700;color:var(--blue);font-size:12px;margin:10px 0 6px}
.pullquote{position:absolute;background:#fff;padding:20px 30px;font-size:9px;line-height:1.6;color:var(--ink);font-weight:600;box-shadow:0 6px 18px rgba(0,0,0,.15)}
.pullquote__open,.pullquote__close{position:absolute;font-family:"Playfair Display",Georgia,serif;font-size:24px;color:var(--ink)}
.pullquote__open{left:8px;top:2px}
.pullquote__close{right:10px;bottom:-6px}
.contact{position:absolute;list-style:none;font-size:9px;color:var(--ink)}
.contact li{display:flex;align-items:center;gap:8px;margin-bottom:7px}
.contact svg{width:12px;height:12px;fill:var(--blue)}
</style>
</head>
<body>
<main class="canvas">

  <!-- Front cover -->
  <section class="sheet sheet--single" style="top:63px">
    <div class="page">
      <div class="url">www.morganhalecoaching.com</div>
      <div class="brand" style="left:34px;top:40px"><span class="brand__mark"></span><span class="brand__name">Morgan Hale</span></div>
      <div class="photo" style="left:0;top:92px;width:500px;height:340px" role="img" aria-label="Photo of two businessmen working together at a laptop in a bright office"></div>
      <div class="band" style="left:236px;top:330px;width:230px">Power of<br>positive thinking</div>
      <div class="rule" style="left:34px;top:488px;width:432px"></div>
      <h1 class="title" style="left:34px;top:510px"><span class="title__main">Coaching Session</span><span class="title__date">June 2018</span></h1>
    </div>
  </section>

  <!-- Spread 1: About / Yesterday Today Tomorrow -->
  <section class="sheet sheet--spread" style="top:833px">
    <div class="page">
      <div class="quote" style="left:30px;top:30px;width:230px;height:190px">
        <span class="quote__mark">“</span>
        I would highly recommend Morgan to any sales professional that is serious about wanting to the next level.
        <span class="quote__by">— Senior Sales Agent, Riverside</span>
      </div>
      <div class="photo" style="left:260px;top:30px;width:210px;height:190px" role="img" aria-label="Photo of the coach presenting at a flip chart"></div>
      <h2 class="heading" style="left:30px;top:250px">About</h2>
      <div class="copy" style="left:30px;top:286px;width:440px">
        <p>Morgan Hale has spent two decades helping agents grow steady results. His sessions focus on clear habits, honest reviews and simple systems that keep every month on track and moving forward.</p>
        <p>Each coaching session looks back at what worked, what slipped and what needs to change next. The aim is a calm plan for the weeks ahead, built around your own goals and the market you serve.</p>
        <p>Clients leave with a short list of actions, a measured pipeline and the confidence to keep showing up, whatever the season brings to their local market and their business.</p>
        <p>Use this agenda as a guide, bring your numbers, and be ready to talk openly about the month that has passed.</p>
      </div>
      <div class="brand brand--sm" style="left:30px;bottom:28px"><span class="brand__mark"></span><span class="brand__name">Morgan Hale</span></div>
    </div>
    <div class="page">
      <h2 class="section-title" style="left:34px;top:40px">Yesterday ~ Today<br>Tomorrow</h2>
      <p class="lead" style="left:34px;top:104px;width:430px">Ideas, plans and promises made in the last month: what did you start, what did you finish, and what will you carry forward into the next four weeks?</p>
      <p class="copy" style="left:34px;top:160px;width:430px;font-weight:700;color:var(--ink);font-size:8.5px">2018/19 Productivity Ideas: There's more to it than numbers</p>
      <ol class="ideas" style="left:34px;top:186px;width:430px">
        <li><span class="ideas__num">1</span>Review last month</li>
        <li><span class="ideas__num">2</span>Set weekly targets</li>
        <li><span class="ideas__num">3</span>Update your database</li>
        <li><span class="ideas__num">4</span>Call past clients</li>
        <li><span class="ideas__num">5</span>Plan open homes</li>
        <li><span class="ideas__num">6</span>Refresh your profile</li>
        <li><span class="ideas__num">7</span>Book appraisals early</li>
        <li><span class="ideas__num">8</span>Track every lead</li>
        <li><span class="ideas__num">9</span>Ask for referrals</li>
        <li><span class="ideas__num">10</span>Write handwritten notes</li>
        <li><span class="ideas__num">11</span>Time block mornings</li>
        <li><span class="ideas__num">12</span>Prepare market reports</li>
        <li><span class="ideas__num">13</span>Follow up buyers</li>
        <li><span class="ideas__num">14</span>Measure conversions</li>
        <li><span class="ideas__num">15</span>Rest and recharge</li>
        <li><span class="ideas__num">16</span>Celebrate small wins</li>
      </ol>
      <div class="brand brand--sm" style="left:34px;bottom:28px"><span class="brand__mark"></span><span class="brand__name">Morgan Hale</span></div>
      <div class="footer-bar" style="left:300px;width:200px"></div>
    </div>
  </section>

  <!-- Spread 2: Pipeline / Questions -->
  <section class="sheet sheet--spread" style="top:1603px">
    <div class="page">
      <div class="photo photo--warm" style="left:30px;top:30px;width:440px;height:300px" role="img" aria-label="Photo of the coach shaking hands with a young agent across a desk"></div>
      <div class="callout" style="left:220px;top:262px;width:230px">Build the listing pipeline so you have stock coming to market when the sun shines again</div>
      <div class="copy" style="left:30px;top:370px;width:420px;font-size:9px;color:var(--ink);font-weight:600">
        <p>Don't wait until the usual "spring selling season" promo's start to start looking for listings.</p>
        <p>Get the jump on your competition by having your July to December pipeline full now, so every week of the warmer months is busy and your income stays steady.</p>
      </div>
      <div class="brand brand--sm" style="left:30px;bottom:28px"><span class="brand__mark"></span><span class="brand__name">Morgan Hale</span></div>
      <div class="footer-bar" style="left:0;width:200px"></div>
    </div>
    <div class="page">
      <ol class="questions" style="left:34px;top:40px;width:430px">
        <li>1. What went well this month?</li>
        <li>2. Did you convert good days into good weeks, good weeks into a good month?</li>
        <li>3. How motivated were you this month?</li>
        <li>4. What ideas, plans and processes have you improved in your business since we last spoke?</li>
        <li>5. What systems do you need to implement to create a smoother work flow?</li>
        <li>6. Are you pursuing what you believe is your true potential?</li>
        <li>7. What have been your numbers for May?
          <ul class="checklist">
            <li>Appraisals booked</li><li>Listings taken</li><li>Open homes held</li><li>Offers written</li><li>Sales settled</li><li>New contacts added</li><li>Referrals received</li><li>Hours prospecting</li>
          </ul>
        </li>
        <li>8. Sales session — what was the best script you used last month?</li>
        <li>9. Stock review</li>
      </ol>
      <div class="photo" style="left:260px;top:470px;width:200px;height:110px" role="img" aria-label="Photo of two people shaking hands over paperwork"></div>
      <div class="footer-bar" style="left:300px;width:200px"></div>
    </div>
  </section>

  <!-- Spread 3: Uncommon common -->
  <section class="sheet sheet--spread" style="top:2373px">
    <div class="page">
      <div class="photo photo--warm" style="left:30px;top:30px;width:440px;height:190px" role="img" aria-label="Photo of business partners shaking hands in a sunlit office"></div>
      <div class="questions" style="left:30px;top:240px;width:440px">
        <div class="subhead" style="font-size:14px">12. Make the uncommon common</div>
        <div class="copy" style="position:static;margin-bottom:8px">
          <p>Look at the small habits top agents repeat every single day. What could you add to your routine from July that most people in your office will skip? Write three ideas below and commit to one.</p>
          <p>1. Daily calls &nbsp; 2. Weekly notes &nbsp; 3. Monthly review</p>
        </div>
        <div class="subhead">What are your behaviours holding you</div>
        <div class="copy" style="position:static">
          <p>Be honest about the patterns that slow you down: late starts, missed follow ups, avoiding hard calls. Name them, then choose one simple swap you will practise for the next thirty days.</p>
          <p>Team focus: share your swap with a colleague and check in with each other every Friday. Small changes, kept up, make a large difference over a year.</p>
        </div>
      </div>
      <div class="footer-bar" style="left:0;width:200px"></div>
    </div>
    <div class="page">
      <div class="photo photo--dark" style="left:0;top:0;width:500px;height:707px" role="img" aria-label="Photo of a businessman in a suit walking across a busy office floor"></div>
      <blockquote class="pullquote" style="left:50px;top:560px;width:400px">
        <span class="pullquote__open">“</span>
        Success is not built in a single big moment. It comes from the small actions you repeat each day, long after the excitement of starting has passed.
        <span class="pullquote__close">”</span>
      </blockquote>
    </div>
  </section>

  <!-- Outer spread: back and front cover -->
  <section class="sheet sheet--spread" style="top:3143px">
    <div class="page">
      <div class="brand" style="left:300px;top:40px"><span class="brand__mark"></span><span class="brand__name">Morgan Hale</span></div>
      <div class="photo" style="left:0;top:110px;width:500px;height:340px" role="img" aria-label="Photo of a team meeting around a laptop in a modern office"></div>
      <div class="brand" style="left:34px;top:520px"><span class="brand__mark"></span><span class="brand__name">Morgan Hale</span></div>
      <ul class="contact" style="left:34px;top:580px">
        <li><svg viewBox="0 0 24 24"><path d="M2 5h20v14H2z M2 5l10 8 10-8" fill="none" stroke="#3a9ad9" stroke-width="2"/></svg>hello@morganhalecoaching.com</li>
        <li><svg viewBox="0 0 24 24"><path d="M6 2l4 5-2 3c1 3 3 5 6 6l3-2 5 4-3 4C10 22 2 14 2 5z"/></svg>+61 400 123 456</li>
        <li><svg viewBox="0 0 24 24"><path d="M12 2a7 7 0 0 0-7 7c0 5 7 13 7 13s7-8 7-13a7 7 0 0 0-7-7zm0 10a3 3 0 1 1 0-6 3 3 0 0 1 0 6z"/></svg>PO Box 210, Riverside WA 6150</li>
      </ul>
    </div>
    <div class="page" style="border-left:none">
      <div class="url">www.morganhalecoaching.com</div>
      <div class="photo" style="left:0;top:110px;width:500px;height:340px" role="img" aria-label="Photo of two businessmen working together at a laptop"></div>
      <div class="band" style="left:236px;top:340px;width:230px">Power of<br>positive thinking</div>
      <div class="rule" style="left:34px;top:500px;width:432px"></div>
      <h2 class="title" style="left:34px;top:520px"><span class="title__main">Coaching Session</span><span class="title__date">June 2018</span></h2>
    </div>
  </section>

</main>
</body>
</html>
```